Create a Poster for a True Crime Tour

Velvet Hook True Crime Tour Poster Design

We need a square and a4 sized poster to promote a true crime tour.

The tour covers stories from 1920s-1930s australia in a period known as the velvet hook wars. The leader of the gang in those days was a female (hence the uploaded image).

Feel free to use this image or find one of your own choosing - I am interested in seeing your interpretation.

Key words that may help trigger ideas (I'm sure there are others I haven't thought of!!):-
scar
razor
torn paper
old film
1920s
border
the gange leader was a female
velvet hook true crime tour
australia
scratch marks

Target Market(s)

20-55 Age Group (70% female)

Industry/Entity Type

Tour

Requirements
Must have
• Include the following phrases:-
• Velvet Hook
• True Crime Tour

```html
<!DOCTYPE html>
<html lang="en">
<head>
<meta charset="utf-8">
<title>Velvet Hook True Crime Tour</title>
<link href="https://fonts.googleapis.com/css2?family=Abril+Fatface&family=Montserrat:wght@700;800;900&family=Open+Sans:ital,wght@1,300&display=swap" rel="stylesheet">
<style>
  :root {
    --ink: #111111;
    --paper: #ffffff;
    --blood: #7b1d27;
    --photo-light: #d9d9d6;
    --photo-mid: #a7a6a2;
    --photo-dark: #3a3a3a;
    --badge: #0b0b0b;
  }
  * { margin: 0; padding: 0; box-sizing: border-box; }
  html, body { width: 800px; height: 1200px; overflow: hidden; background: var(--paper); }
  .poster {
    position: relative;
    width: 800px;
    height: 1200px;
    background: var(--paper);
    overflow: hidden;
    font-family: "Montserrat", sans-serif;
    color: var(--ink);
  }
  .info-column {
    position: absolute;
    left: 0; top: 0;
    width: 428px; height: 1200px;
  }
  .title {
    position: absolute;
    left: 0; top: 82px;
    width: 428px;
    text-align: center;
    font-family: "Abril Fatface", serif;
    font-weight: 400;
    font-size: 74px;
    line-height: 94px;
    letter-spacing: 1px;
    color: transparent;
    background: repeating-linear-gradient(180deg, var(--ink) 0 2px, var(--paper) 2px 4.5px);
    -webkit-background-clip: text;
    background-clip: text;
    -webkit-text-stroke: 2px var(--ink);
  }
  .title span { display: block; }
  .years {
    position: absolute;
    left: 0; top: 280px;
    width: 428px;
    text-align: center;
    font-weight: 800;
    font-size: 24px;
    letter-spacing: -0.5px;
  }
  .tour-frame {
    position: absolute;
    left: 110px; top: 375px;
    width: 203px; height: 181px;
  }
  .tour-frame .corner {
    position: absolute;
    border-color: var(--ink);
    border-style: solid;
  }
  .tour-frame .corner-top { left: 0; top: 0; width: 110px; height: 102px; border-width: 2px 0 0 2px; }
  .tour-frame .corner-bottom { right: 0; bottom: 0; width: 130px; height: 62px; border-width: 0 2px 2px 0; }
  .tour-name {
    position: absolute;
    left: 26px; top: 20px;
    width: 160px;
    text-align: center;
    font-weight: 900;
    line-height: 0.95;
    letter-spacing: -1.5px;
  }
  .tour-name .big { display: block; font-size: 54px; }
  .tour-name .mid { display: block; font-size: 44px; }
  .tour-name .end { display: block; font-size: 48px; }
  .law-quote {
    position: absolute;
    left: 0; top: 612px;
    width: 400px;
    text-align: center;
    font-weight: 800;
    font-size: 22px;
    line-height: 41px;
    letter-spacing: -0.3px;
  }
  .law-quote .stress { font-size: 31px; }
  .law-source {
    position: absolute;
    right: 26px; top: 780px;
    font-family: "Open Sans", sans-serif;
    font-style: italic;
    font-weight: 300;
    font-size: 20px;
    color: #333333;
  }
  .tagline {
    position: absolute;
    left: 40px; top: 955px;
    width: 340px;
    text-align: right;
    font-weight: 800;
    font-size: 33px;
    line-height: 52px;
    letter-spacing: -0.5px;
  }
  .tagline .blood { color: var(--blood); font-size: 42px; }
  .portrait {
    position: absolute;
    left: 428px; top: 0;
    width: 372px; height: 1200px;
    background:
      radial-gradient(ellipse 60% 35% at 80% 55%, #ececea 0%, rgba(236,236,234,0) 70%),
      radial-gradient(ellipse 70% 25% at 80% 12%, var(--photo-dark) 0%, rgba(58,58,58,0) 80%),
      radial-gradient(ellipse 25% 30% at 10% 65%, rgba(123,29,39,0.55) 0%, rgba(123,29,39,0) 80%),
      linear-gradient(90deg, var(--photo-mid) 0%, var(--photo-light) 45%, #e6e6e4 100%);
  }
  .brand-badge {
    position: absolute;
    left: 604px; top: 1088px;
    width: 174px; height: 96px;
    border-radius: 50%;
    background: var(--badge);
    display: flex;
    align-items: center;
    justify-content: center;
  }
  .brand-badge span {
    font-weight: 700;
    font-size: 15px;
    color: var(--paper);
    letter-spacing: 0.3px;
  }
</style>
</head>
<body>
  <main class="poster">
    <section class="info-column">
      <h1 class="title"><span>VELVET</span><span>HOOKS</span></h1>
      <p class="years">1927-1931</p>
      <div class="tour-frame">
        <div class="corner corner-top"></div>
        <div class="corner corner-bottom"></div>
        <h2 class="tour-name"><span class="big">TRUE</span><span class="mid">CRIME</span><span class="end">TOUR</span></h2>
      </div>
      <blockquote class="law-quote">
        “A person shall <span class="stress">not</span><br>
        <span class="stress">purchase, carry,</span><br>
        or have in his <span class="stress">possession</span><br>
        any <span class="stress">pistol...”</span>
      </blockquote>
      <p class="law-source">Pistol Licensing Act of 1927</p>
      <p class="tagline">... they <span class="blood">killed</span> with<br><span class="blood">razors</span> instead.</p>
    </section>
    <div class="portrait" role="img" aria-label="Black and white portrait of a 1920s woman with red eye and lips holding a straight razor, blood splatters on a stone wall"></div>
    <div class="brand-badge"><span>NIGHT LEDGER</span></div>
  </main>
</body>
</html>
```